VelaMarina Passport 4 Page A5 Brochure

DESIGN BRIEF – VelaMarina Passport Brochure
Project Title
VelaMarina Passport – A5 4-Page Brochure Design
________________________________________
Overview
We are looking for a designer to create a clean, visually appealing A5, 4-page brochure to present The VelaMarina Passport to local businesses.
The brochure will be used as a sales and information document and should feel:
• Premium
• Friendly
• Professional
• Easy to understand
• Fun and engaging
The audience is bar owners, venue managers, restaurants, clubs, hotels, and local businesses in Maspalomas.
Format & Technical Requirements
• Size: A5
• Pages: 4 (front cover, 2 inside pages, back cover)
• Orientation: Portrait
• Print-ready design
• Space-aware layouts (some content will be added later)
Brand & Tone
• Brand: VelaMarina
• Location: Maspalomas / Gran Canaria
• Target audience: LGBTQ+ friendly venues and tourism businesses
• Style:
o Modern
o Warm
o Professional
o Island-inspired
o Not overly corporate
• Avoid clutter — white space is welcome
PAGE-BY-PAGE REQUIREMENTS
PAGE 1 – FRONT COVER
Purpose: First impression & visual impact
Requirements:
• Strong visual design
• Clear title: “The VelaMarina Passport”
• Subheading example:
A premium voucher booklet connecting tourists with local venues
• Leave a clear placeholder space for:
o An image of the Passport front cover
• We are open to designers also proposing a design for the Passport front cover itself (optional extra – happy to receive bids for this)
Style notes:
• Eye-catching but elegant
• Feel of travel, discovery, nightlife, and local culture
PAGE 2 – INSIDE LEFT
Purpose: Explain the concept – text provided
Content:
• Short overview of:
o What The VelaMarina Passport is
o Targeted distribution
o Key benefits (high-value visitors, no wasted reach, transferable, no expiry)
• Icons or visual blocks encouraged
• Easy-to-scan layout
Design Notes:
• Use headings, icons, or info blocks
• Avoid large walls of text
PAGE 3 – INSIDE RIGHT (How the Passport Works in Practice)
Purpose:
To visually explain how The VelaMarina Passport is owned, transferred, and used, while showing real examples of how venues appear inside the booklet.
Required Elements
1. Passport Ownership & Transfer Section
The Passport can be owned by up to three people in total (original owner + two transfers).
This page should include three clearly defined visual placeholders representing:
• Original Passport Owner
• Transfer 1 – New Owner
• Transfer 2 – Final Owner
These can be shown as:
• Three mini page mockups
• Three outlined boxes with headings
• Or a creative, passport-style visual layout
Each section should clearly show space for:
• Name
• Country (optional)
• Signature
• Date
👉 We are open to creative proposals for the design of this transfer page and happy to receive bids specifically for designing this page as part of the Passport.
2. Example Voucher Advert Section
This page should also include space to show an example of a voucher advert page, displayed as a mock layout only.
The example should visually communicate:
• Venue name & logo
• Short venue description
• Example offer (e.g. “Free signature shot”)
• Voucher box to be crossed off by staff
This is illustrative only — final content will be provided later.
Design Notes
• Keep the layout clear and easy to understand at a glance
• Visual explanation is more important than text
• Use icons, borders, or soft background panels to separate sections
• The tone should feel official but friendly, similar to a real passport
• Avoid clutter — white space is encouraged
Key Message to Communicate Visually
• The Passport has real ownership
• It can be passed on
• Vouchers are clearly controlled
• Each page feels premium, structured, and easy to use
PAGE 4 – BACK COVER
Purpose: Commercial offer & call to action
Content requirements:
• Clear presentation of two participation options:
1. Voucher Page (incentivised pricing)
2. Standard Advertising Page (no voucher)
• Simple comparison layout encouraged
Visual placeholders required:
• Space to show:
o A sample voucher page
o A sample advert-only page
Contact Details Area:
• VelaMarina logo or name
• Contact text placeholder (phone / email / website)
• Clean, professional call to action
Design Flexibility
We are happy to:
• Receive creative layout suggestions
• See optional icon sets
• See colour palette ideas
• Receive proposals that slightly refine the structure (as long as all elements are included)
Deliverables
• Final A5 4-page brochure design
• Print-ready PDF
• Editable source files (preferred)
• Clear indication of any optional extras (e.g. Passport cover design)
What We’re Looking For
• Clean layout
• Strong hierarchy
• Clear visual storytelling
• Understanding of hospitality / nightlife / tourism
• Ability to balance fun with professionalism
Optional Extras (welcome but not required)
• Proposal for the Passport front cover design
• Proposal for the transfer page design
• Icon set or mini graphic elements
• Alternative colour version
Notes to Designers
This brochure will be used repeatedly and updated over time, so clarity, flexibility, and strong structure are more important than heavy decoration.
We look forward to creative, thoughtful proposals.

Target Market(s)

LGBTIQ+ Tourists and Businesses

Industry/Entity Type

Tourism

Requirements
Must have
• meet the 4 page brief
Nice to have
• proposals for design elements within the design

```html
<!DOCTYPE html>
<html lang="en">
<head>
<meta charset="utf-8">
<title>VelaMarina Passport – Commercial Offer</title>
<link href="https://fonts.googleapis.com/css2?family=Tomorrow:wght@500;600&family=Outfit:wght@300;400;500;600&display=swap" rel="stylesheet">
<style>
  :root {
    --ink: #0b0b0b;
    --text: #3a3a3a;
    --grey-bg: #e6e7e9;
    --pill: #ececec;
    --rule: #cfcfcf;
    --blue: #2f80d1;
    --sun-top: #f3a214;
    --sun-mid: #f6e52a;
    --sun-low: #e5541f;
    --white: #ffffff;
  }
  * { margin: 0; padding: 0; box-sizing: border-box; }
  html, body { width: 839px; height: 1200px; overflow: hidden; background: var(--white); }
  .page {
    position: relative; width: 839px; height: 1200px; overflow: hidden;
    font-family: "Outfit", sans-serif; color: var(--text); background: var(--white);
  }
  .hero-art { position: absolute; inset: 0; width: 839px; height: 720px; }
  .title {
    position: absolute; left: 54px; top: 552px;
    font-family: "Tomorrow", sans-serif; font-weight: 600;
    font-size: 49px; line-height: 50px; color: var(--ink); letter-spacing: 0.5px;
    text-transform: uppercase;
  }
  .offer-photo {
    position: absolute; top: 730px; width: 153px; height: 136px; border-radius: 12px;
  }
  .offer-photo.venue-dining { left: 54px; background: linear-gradient(160deg, #9fb4c4 0%, #e9e4dc 45%, #c9a57e 75%, #4a4e52 100%); }
  .offer-photo.venue-garden { left: 424px; background: linear-gradient(160deg, #d9c8a0 0%, #5b5047 35%, #4f7a3a 70%, #2f5a23 100%); }
  .offer { position: absolute; top: 742px; }
  .offer.best-value { left: 230px; }
  .offer.standard { left: 600px; }
  .offer h2 {
    font-family: "Tomorrow", sans-serif; font-weight: 500; font-size: 20px; line-height: 20px;
    color: var(--ink); text-transform: uppercase; margin-bottom: 9px;
  }
  .offer ul { list-style: none; }
  .offer li {
    position: relative; padding-left: 10px; font-size: 9.6px; font-weight: 300;
    line-height: 10.5px; margin-bottom: 5.5px; color: var(--text);
  }
  .offer li::before {
    content: ""; position: absolute; left: 0; top: 3px; width: 5px; height: 5px;
    border-radius: 50%; background: var(--blue);
  }
  .offer .cost { position: absolute; top: 104px; white-space: nowrap; font-size: 7.6px; font-weight: 600; color: var(--text); }
  .divider { position: absolute; left: 37px; top: 914px; width: 765px; height: 1px; background: var(--rule); }
  .pricing-title {
    position: absolute; left: 0; width: 839px; top: 936px; text-align: center;
    font-family: "Tomorrow", sans-serif; font-weight: 500; font-size: 30px; color: var(--ink);
    text-transform: uppercase;
  }
  .terms { position: absolute; left: 141px; top: 981px; display: grid; grid-template-columns: 275px 275px; gap: 6px 7px; }
  .term {
    height: 33px; border-radius: 17px; background: var(--pill);
    padding-left: 28px; display: flex; align-items: center;
    font-size: 7.6px; font-weight: 500; color: var(--text);
  }
  .brand { position: absolute; left: 64px; top: 1108px; display: flex; align-items: center; gap: 8px; }
  .brand-dot { width: 22px; height: 22px; border-radius: 50%; background: var(--blue); }
  .brand-name { font-family: "Outfit", sans-serif; font-weight: 500; font-size: 24px; color: var(--blue); }
  .contact { position: absolute; top: 1105px; display: flex; align-items: center; gap: 7px; }
  .contact.phone { left: 311px; }
  .contact.email { left: 471px; }
  .contact.web { left: 640px; }
  .contact-icon { width: 34px; height: 34px; border-radius: 50%; background: var(--blue); display: flex; align-items: center; justify-content: center; }
  .contact-icon svg { width: 14px; height: 14px; }
  .contact-label { font-size: 9.6px; line-height: 12px; }
  .contact-label strong { display: block; font-weight: 600; color: #555; }
  .contact-label span { font-weight: 400; color: var(--text); }
</style>
</head>
<body>
<main class="page">
  <svg class="hero-art" viewBox="0 0 839 720" aria-hidden="false">
    <defs>
      <linearGradient id="sunsetTone" x1="0" y1="0" x2="0" y2="1">
        <stop offset="0" stop-color="var(--sun-top)"/>
        <stop offset="0.45" stop-color="#f4b21c"/>
        <stop offset="0.6" stop-color="var(--sun-mid)"/>
        <stop offset="0.82" stop-color="var(--sun-low)"/>
        <stop offset="1" stop-color="#1a0d06"/>
      </linearGradient>
      <filter id="softShadow" x="-10%" y="-10%" width="120%" height="120%">
        <feDropShadow dx="-4" dy="6" stdDeviation="8" flood-color="#000" flood-opacity="0.18"/>
      </filter>
    </defs>
    <path class="grey-sweep" d="M0 0 H839 V700 C620 700 420 560 250 420 C150 340 60 270 0 200 Z" fill="var(--grey-bg)"/>
    <circle class="white-ring" cx="836" cy="115" r="582" fill="var(--white)" filter="url(#softShadow)"/>
    <circle class="sunset-scene" cx="836" cy="115" r="549" fill="url(#sunsetTone)" role="img" aria-label="Tropical sunset with palm tree silhouettes against an orange and yellow sky"/>
  </svg>

  <h1 class="title">Commercial<br>Offer and Call<br>to Action</h1>

  <div class="offer-photo venue-dining" role="img" aria-label="Photo of an elegant waterfront dining room set for an event"></div>
  <section class="offer best-value">
    <h2>Best Value</h2>
    <ul>
      <li>Full A6 advert</li>
      <li>Venue branding &amp; details</li>
      <li>Fun, venue-specific offer</li>
      <li>Voucher box for staff to mark</li>
    </ul>
    <p class="cost">Cost: €50–€100 per page per print batch</p>
  </section>

  <div class="offer-photo venue-garden" role="img" aria-label="Photo of a garden terrace venue with a chalkboard sign"></div>
  <section class="offer standard">
    <h2>Standard<br>Advertising</h2>
    <ul>
      <li>Brand exposure only</li>
      <li>Placements: back page, inside covers,<br>centre spread</li>
    </ul>
    <p class="cost">Cost: €100–€500 depending on placement</p>
  </section>

  <div class="divider"></div>

  <h2 class="pricing-title">Pricing Model</h2>
  <div class="terms">
    <div class="term">Based on 2,000 copies per print batch</div>
    <div class="term">Participation confirmed per edition</div>
    <div class="term">No long-term commitment</div>
    <div class="term">Venues can update adverts or offers each edition</div>
  </div>

  <div class="brand">
    <div class="brand-dot"></div>
    <div class="brand-name">VelaMarina</div>
  </div>

  <div class="contact phone">
    <div class="contact-icon">
      <svg viewBox="0 0 24 24"><path fill="#fff" d="M6.6 10.8c1.4 2.8 3.8 5.1 6.6 6.6l2.2-2.2c.3-.3.7-.4 1-.2 1.1.4 2.3.6 3.6.6.6 0 1 .4 1 1V20c0 .6-.4 1-1 1C10.6 21 3 13.4 3 4c0-.6.4-1 1-1h3.5c.6 0 1 .4 1 1 0 1.3.2 2.5.6 3.6.1.3 0 .7-.2 1z"/></svg>
    </div>
    <div class="contact-label"><strong>Phone:</strong><span>123 (456) 7890</span></div>
  </div>
  <div class="contact email">
    <div class="contact-icon">
      <svg viewBox="0 0 24 24"><path fill="#fff" d="M3 6h18v12H3z"/><path fill="none" stroke="#2f80d1" stroke-width="1.6" d="M3 6l9 7 9-7"/></svg>
    </div>
    <div class="contact-label"><strong>Email:</strong><span>Info@example.com</span></div>
  </div>
  <div class="contact web">
    <div class="contact-icon">
      <svg viewBox="0 0 24 24"><circle cx="12" cy="12" r="9" fill="none" stroke="#fff" stroke-width="2"/><path fill="none" stroke="#fff" stroke-width="1.6" d="M3 12h18M12 3c3 3 3 15 0 18M12 3c-3 3-3 15 0 18"/></svg>
    </div>
    <div class="contact-label"><strong>Website::</strong><span>VelaMarina Passport</span></div>
  </div>
</main>
</body>
</html>
```